Cutting edge Software Development Company needs to revamp it's website to reflect its growth ...

We would like to have our company website redone to have a more executive clean feel while still maintaining some level of playfulness. We currently offer bespoke Software's for Microfinance organizations on phone/mobile and Internet. Our development services could extend to selling you a platform outright or offering the platform as a service on either mobile or internet. Our corporate colors are Blue and White and we would like to see this reflected in the overall design. The final design should reflect a company thats making strides by helping our customers ideas come to life" a listening and caring partner!Current website: https://voltrix.co.ke/

Target Market(s)

Microfinance institutions that have a good customer base but do not have a back end or front end to support customers acquisition and servicing

Industry/Entity Type

Software Development

Number of Pages Required

5+ page

Font styles to use
Sans Serif

Colors
0255a3
0792cd
ffffff
cedeed
eaf1f7

Requirements
Must have
• Creative design
• Clean design
• Easy to navigate from page to page
Nice to have
• Blogs and Testimonials
Should not have
• Anything that would promote religious bias or show that we are not open to doing business with everyone.

```html
<!DOCTYPE html>
<html lang="en">
<head>
<meta charset="utf-8">
<title>Voltrix Technologies</title>
<link href="https://fonts.googleapis.com/css2?family=Open+Sans:wght@400;600;700&display=swap" rel="stylesheet">
<style>
:root{
  --blue:#0255a3;
  --blue-dark:#0a3f86;
  --sky:#0792cd;
  --white:#ffffff;
  --mist:#cedeed;
  --pale:#eaf1f7;
  --ink:#1a1a1a;
  --text:#3d3d3d;
  --grey:#8a8a8a;
}
*{margin:0;padding:0;box-sizing:border-box}
html,body{width:1200px;height:3317px;overflow:hidden}
body{position:relative;font-family:"Open Sans",sans-serif;color:var(--text);background:var(--white)}
.abs{position:absolute}
.topbar{left:0;top:0;width:1200px;height:33px;background:var(--blue);color:var(--white);font-size:12px}
.topbar span{position:absolute;top:9px}
.nav{left:0;top:33px;width:1200px;height:82px;background:var(--white)}
.brand{left:116px;top:22px;display:flex;align-items:center;gap:8px;font-weight:700;font-size:22px;color:var(--blue)}
.brand i{width:26px;height:26px;border-radius:50%;background:var(--sky);display:block}
.nav a{position:absolute;top:31px;font-size:10.5px;font-weight:700;color:var(--ink);text-decoration:none;letter-spacing:.2px}
.btn{display:flex;align-items:center;justify-content:center;background:var(--blue);color:var(--white);font-weight:700;font-size:11px;letter-spacing:.8px;text-decoration:none}
.hero{left:0;top:115px;width:1200px;height:525px;background:linear-gradient(100deg,#0a4a98 0%,#1f63ad 45%,#3a78b8 70%,#1b5aa5 100%)}
.hero h1{position:absolute;left:108px;top:140px;width:520px;font-size:39px;line-height:51px;font-weight:700;color:var(--white)}
.hero p{position:absolute;left:108px;top:263px;width:500px;font-size:20px;line-height:28px;color:var(--white)}
.card{top:551px;width:233px;height:364px;background:var(--white);box-shadow:0 2px 10px rgba(0,0,0,.08);padding:30px 25px}
.card h3{font-size:14.5px;font-weight:700;color:var(--ink);margin-bottom:23px}
.card p{font-size:11.6px;line-height:19.2px;color:var(--text)}
.about h2{position:absolute;left:108px;top:1020px;width:400px;font-size:17.5px;line-height:23px;font-weight:700;color:var(--ink)}
.about p{position:absolute;left:108px;top:1104px;width:456px;font-size:11.6px;line-height:19.2px}
.arrow{top:1286px;width:40px;height:36px;background:var(--blue)}
.slide{top:1020px;height:346px;padding:32px 22px;color:var(--white);box-shadow:0 2px 8px rgba(0,0,0,.15)}
.slide h3{font-size:19px;font-weight:700;margin-bottom:30px}
.slide p{font-size:12px;line-height:19.2px}
.highlights{left:0;top:1470px;width:1200px;height:629px;background:var(--pale)}
.highlights h2{position:absolute;left:0;top:57px;width:1200px;text-align:center;font-size:30px;font-weight:700;color:var(--ink)}
.project h3{position:absolute;left:717px;top:1683px;font-size:21px;font-weight:700;color:var(--ink)}
.project p{position:absolute;left:717px;width:360px;font-size:11.8px;line-height:19.2px}
.partner{top:2282px;height:60px;display:flex;align-items:center;gap:8px;font-size:19px;font-weight:700;color:#7d7d7d}
.partner i{width:34px;height:34px;border-radius:50%;background:#a9a9a9;display:block;flex:none}
.cta{left:0;top:2400px;width:1200px;height:917px;background:linear-gradient(180deg,#ffffff 0%,#e3ebf5 8%,#8fafd7 25%,#3f77c1 45%,#1a5ab0 62%,#0f52a6 100%)}
.cta h2{position:absolute;left:0;top:80px;width:1200px;text-align:center;font-size:40px;font-weight:700;color:var(--ink)}
.foot h4{position:absolute;top:3138px;font-size:11.5px;font-weight:700;color:var(--white);letter-spacing:.3px}
.foot p,.foot a{position:absolute;font-size:9.5px;line-height:16px;color:var(--white);letter-spacing:.6px;text-decoration:none}
</style>
</head>
<body>

<div class="abs topbar">
  <span style="left:836px">(254) 700 555 014</span>
  <span style="left:1000px">info@voltrix.co.ke</span>
</div>

<header class="abs nav">
  <div class="abs brand"><i></i>Voltrix</div>
  <a style="left:291px">HOME</a>
  <a style="left:363px">ABOUT US</a>
  <a style="left:452px">SERVICES</a>
  <a style="left:528px">OUR GOALS</a>
  <a style="left:617px">PARTNERS</a>
  <a style="left:707px">DEMO</a>
  <a style="left:792px">PRICES</a>
  <a style="left:869px">POLICIES</a>
  <a class="abs btn" style="left:967px;top:20px;width:125px;height:33px;color:var(--white)">GET IN TOUCH</a>
</header>

<section class="abs hero" role="img" aria-label="Hands typing on a laptop keyboard under a blue overlay">
  <h1>Welcome to the World of Innovation</h1>
  <p>Voltrix Technologies helps you to add value to your everyday Ideas.</p>
</section>

<article class="abs card" style="left:108px">
  <h3>CLOUD SERVICES</h3>
  <p>Voltrix Cloud Services can dynamically scale to meet the needs of its users, and because the service provider supplies the hardware and software necessary for the service, there's no need for a company to provision or deploy its own resources or allocate IT staff to manage the service.</p>
</article>
<article class="abs card" style="left:358px">
  <h3>MOBILE APPLICATIONS</h3>
  <p>Voltrix Technologies provide a range of mobile solutions include Android Apps, IOS Apps, USSD. This provides alternative channels for customers to access various services including but not limited to Balance Enquiry, Loan Application, Agent/Field Officer cash withdraw and deposit, Agent/ Field Officer Customer creation, Account Opening among others.</p>
</article>
<article class="abs card" style="left:608px">
  <h3>MOBILE MONEY</h3>
  <p>Voltrix also offers integration to Mobile platform like MobiPay, TelCash etc. The integrations ranges from Business-to-Business (B2B), Business-to-Customer (B2C) and Customer-to-Business (C2B). The integration allows Instant Payment Notification (IPN) whenever a transaction is completed.</p>
</article>
<article class="abs card" style="left:859px">
  <h3>BULK SMS</h3>
  <p>Voltrix Technologies provide integration to bulk sms provider for PUSH and PULL sms services. Bulk SMS solution include and interface for managing the service including defining new campaigns, sending direct messages and reports.</p>
</article>

<section class="about">
  <h2>Voltrix Technologies LTD is a specialized IT company focused on end-to-end solutions for the financial sector.</h2>
  <p>Voltrix Technologies LTD is a privately-owned company, designed to offer both professional consultancy services and development and delivery of software and infrastructure products that enable Sacco institutions to to expand their outreach through the use of suitable technologies. Voltrix Technologies prides itself on delivering products and services that adhere to the principles of quality, transparency and affordability. Voltrix Technologies is comprised of a highly experienced team of professionals, with a track record of developing and implementing financial systems and handling complex development projects.</p>
  <div class="abs arrow" style="left:108px">
    <svg width="40" height="36" viewBox="0 0 40 36"><path d="M25 18H15M19 14l-4 4 4 4" stroke="#fff" stroke-width="1.6" fill="none"/></svg>
  </div>
  <div class="abs arrow" style="left:160px">
    <svg width="40" height="36" viewBox="0 0 40 36"><path d="M15 18h10M21 14l4 4-4 4" stroke="#fff" stroke-width="1.6" fill="none"/></svg>
  </div>
</section>

<div class="abs slide" style="left:606px;width:234px;background:linear-gradient(160deg,#0a4a98,#1d5fae 60%,#2e6cb5)" role="img" aria-label="Developers working at computers under a blue overlay">
  <h3>WE CODE</h3>
  <p>We have cutting edge projects have been designed and managed by the company's development team members, all of which contribute to the current high quality development standards.</p>
</div>
<div class="abs slide" style="left:856px;width:236px;padding-top:26px;background:linear-gradient(160deg,#0d4c9a,#245fa8 55%,#3a73b6)" role="img" aria-label="Project manager at a desk under a blue overlay">
  <h3>WE CREATE</h3>
  <p>The team of project managers in Voltrix Technologies has successfully implemented numerous internatioonal projects that today help to guarantee the structured and efficient delivery of the company solutions.</p>
</div>
<div class="abs slide" style="left:1109px;width:120px;background:linear-gradient(90deg,#2a63ac,#b9cde6);opacity:.85" role="img" aria-label="Team support scene under a blue overlay">
  <h3>WE DE</h3>
  <p>Voltrix Techn support for products a Level Agree are signed main types provided w 1. Investiga documenta</p>
</div>

<section class="abs highlights">
  <h2>Project Highlights</h2>
</section>

<div class="abs" style="left:179px;top:1624px;width:496px;height:475px;background:#ffffff;box-shadow:0 2px 10px rgba(0,0,0,.12);overflow:hidden">
  <div style="height:22px;background:#2b2b2b"></div>
  <div role="img" aria-label="Lending app store listing with screenshots" style="position:absolute;left:0;top:22px;width:496px;height:453px;background:linear-gradient(180deg,#f4f6f9,#e6ebf2)"></div>
</div>
<div class="abs" role="img" aria-label="Lending app sign-in screen on a phone" style="left:109px;top:1745px;width:223px;height:461px;border-radius:30px;background:#1b1b1b">
  <div style="position:absolute;left:16px;top:60px;width:191px;height:322px;background:linear-gradient(180deg,#1d3d7a 0 33%,#ffffff 33%)"></div>
</div>

<section class="project">
  <h3>Kilele Credit Limited</h3>
  <p style="top:1729px">Kilele Credit Limited is Kenya's premier SME and consumer lender. Just like their name, they believe in the hardworking and enterprising nature of our people. They are here to lend you a helping hand because we know a little "push" may be all you need for your business to take off.</p>
  <p style="top:1845px">We give more than money. We take time to understand our clients' needs and we develop a lasting relationship with them on their entrepreneurial journey.</p>
  <a class="abs btn" style="left:717px;top:1937px;width:162px;height:32px">SEE ALL PROJECTS</a>
</section>

<div class="abs partner" style="left:114px"><i></i>Mwanzo Sacco</div>
<div class="abs partner" style="left:334px"><i></i>Kilele Credit</div>
<div class="abs partner" style="left:502px"><i></i>Nuru Ventures</div>
<div class="abs partner" style="left:705px;font-weight:400">Shamba Growth</div>
<div class="abs partner" style="left:890px"><i></i>Mkopo Credit</div>

<section class="abs cta" role="img" aria-label="City skyline fading into blue">
  <h2>Create your next project with us</h2>
  <a class="abs btn" style="left:537px;top:166px;width:125px;height:32px">GET IN TOUCH</a>
</section>

<footer class="foot">
  <h4 style="left:108px">COMPANY</h4>
  <p style="left:108px;top:3168px;width:205px">Voltrix Technologies LTD is a privately-owned company, designed to offer both professional consultancy services and development and delivery of software and infrastructure products</p>
  <h4 style="left:473px;top:3134px">LINKS</h4>
  <a style="left:475px;top:3171px">HOME</a>
  <a style="left:475px;top:3192px">ABOUT US</a>
  <a style="left:475px;top:3213px">SERVICES</a>
  <a style="left:475px;top:3234px">OUR GOALS</a>
  <a style="left:475px;top:3255px">PARTNERS</a>
  <a style="left:561px;top:3181px">DEMO</a>
  <a style="left:561px;top:3202px">PRICES</a>
  <a style="left:561px;top:3223px">POLICIES</a>
  <h4 style="left:775px;top:3134px">CONTACT US</h4>
  <p style="left:775px;top:3168px">Contact Info<br>Riverside Court, Off Ring Rd</p>
  <p style="left:775px;top:3208px">+254 700 555 014<br>info@voltrix.co.ke</p>
  <p style="left:775px;top:3248px">Daily: 9:00 am - 6:00 pm<br>Sunday: Closed</p>
</footer>

</body>
</html>
```